Tall Birch Path newsletter - Mail Chimp

Tall Birch Path - Empowering Life Coach needs Mail Chimp Newsletter Template. This is a newsletter I will send out monthly to current clients and prospective clients to offer (hopefully) inspiring and uplifting content AND to give info and dates of my upcoming workshops and retreats.

I have attached a word document with all of the different sections of the mail chimp template I would like to have - and hte actual content for the first newsletter.

I'd like to look uplifting, fun, inspiring.

I also need it to be easy for me to use to update in the future :)

Target Market(s)

Women - moms

Industry/Entity Type

Life Coaching

Requirements
Nice to have
• Color theme to match my "Tall Birch Path" logo

```html
<!DOCTYPE html>
<html lang="en">
<head>
<meta charset="utf-8">
<title>Tall Birch Path Tips &amp; Tools Newsletter</title>
<link href="https://fonts.googleapis.com/css2?family=Montserrat:wght@400;600;700;800&family=Open+Sans:wght@400;600&family=Great+Vibes&display=swap" rel="stylesheet">
<style>
:root{
  --purple:#5a1f7d;
  --purple-deep:#3b1156;
  --magenta:#b0186e;
  --pink:#e0307e;
  --red:#c8173f;
  --orange:#f39a1e;
  --ink:#3c3c46;
  --white:#ffffff;
  --dark:#2b2b33;
}
*{box-sizing:border-box;margin:0;padding:0}
html,body{width:1200px;height:5128px;overflow:hidden;background:var(--white)}
body{font-family:"Open Sans",Arial,sans-serif;color:var(--ink);position:relative}
.script{font-family:"Great Vibes",cursive;font-weight:400}
.caps{font-family:"Montserrat",Arial,sans-serif;font-weight:800;text-transform:uppercase}

/* Hero */
.hero{position:absolute;top:0;left:0;width:1200px;height:740px;overflow:hidden}
.hero-photo{position:absolute;inset:0;background:linear-gradient(180deg,#f7f0ea 0%,#f8d7a2 38%,#f1a23f 60%,#c9641d 80%,#5c2a14 100%)}
.hero-wash{position:absolute;left:0;top:0;width:760px;height:740px;background:linear-gradient(90deg,rgba(255,255,255,.85),rgba(255,255,255,0))}
.brand{position:absolute;left:70px;top:70px;display:flex;align-items:center;gap:14px;font-family:"Montserrat",sans-serif;font-weight:800;font-size:40px;color:var(--purple)}
.brand-dot{width:34px;height:34px;border-radius:50%;background:var(--orange)}
.hero-title{position:absolute;left:70px;top:380px;font-size:66px;color:var(--purple);letter-spacing:1px;line-height:1}
.hero-sub{position:absolute;left:70px;top:520px;font-size:24px;color:var(--ink)}
.btn{position:absolute;left:70px;top:570px;width:190px;height:66px;background:var(--red);color:var(--white);font:600 20px "Montserrat",sans-serif;display:flex;align-items:center;justify-content:center;border-radius:4px}
.polaroid{position:absolute;background:var(--white);padding:14px 14px 40px;box-shadow:0 6px 18px rgba(0,0,0,.25)}
.polaroid div{width:100%;height:100%}
.pol-a{left:770px;top:520px;width:200px;height:190px;transform:rotate(-7deg)}
.pol-a div{background:linear-gradient(160deg,#f5b04a,#b74f1b)}
.pol-b{left:900px;top:580px;width:230px;height:200px;transform:rotate(6deg)}
.pol-b div{background:linear-gradient(160deg,#c7e0f2,#d89a54)}
.hero-curve{position:absolute;left:0;bottom:0}

/* Letter */
.letter{position:absolute;top:760px;left:0;width:1200px;height:560px;text-align:center}
.quote-mark{font:800 110px "Montserrat",sans-serif;color:var(--purple);line-height:.8;height:70px}
.greeting{font-size:64px;color:var(--magenta);margin-top:4px}
.letter p{font-size:17px;line-height:1.6;text-align:left;margin:16px 90px 0}
.signoff{font-size:62px;color:var(--purple);margin-top:14px}
.blob-left{position:absolute;left:0;top:1300px}
.blob-right{position:absolute;right:0;top:1120px}

/* Building happiness */
.building{position:absolute;top:1350px;left:0;width:1200px;height:760px}
.building-photo{position:absolute;left:100px;top:40px;width:440px;height:660px;border:6px solid var(--white);box-shadow:0 4px 20px rgba(0,0,0,.2);background:linear-gradient(180deg,#e8d9ef 0%,#c9b6dc 35%,#a793c4 55%,#7b6aa3 100%)}
.building-photo .brand{position:static;justify-content:center;margin-top:60px;font-size:34px}
.section-band{position:absolute;left:580px;top:40px;width:620px;height:70px;background:var(--purple);color:var(--white);font:700 34px "Montserrat",sans-serif;padding:12px 30px}
.building-text{position:absolute;left:600px;top:140px;width:520px;font-size:16.5px;line-height:1.6}
.building-text p{margin-bottom:16px}
.building-text ul{margin:0 0 16px 22px}
.deco-swoosh{position:absolute;right:0;top:500px}

/* Questions band */
.questions{position:absolute;top:2160px;left:0;width:1200px;height:580px;background:linear-gradient(135deg,var(--purple-deep) 0%,var(--purple) 50%,var(--magenta) 100%);color:var(--white);display:flex;gap:70px;padding:80px 90px}
.question{flex:1}
.question h3{font-size:30px;line-height:1.3}
.question p{font-size:17px;line-height:1.6;margin-top:34px}

/* Quotes */
.quotes{position:absolute;top:2800px;left:0;width:1200px;display:flex;justify-content:center;gap:60px}
.quote-card{width:440px}
.quote-art{height:500px;display:flex;flex-direction:column;justify-content:center;padding:40px;color:var(--white)}
.quote-art.one{background:linear-gradient(180deg,#4a5356,#2e3538 60%,#6d5a3a)}
.quote-art.two{background:linear-gradient(180deg,#3b3d3f,#262829 60%,#555b5c)}
.quote-art blockquote{font:800 38px/1.15 "Montserrat",sans-serif;text-transform:uppercase}
.quote-art.two blockquote{font-size:29px;text-align:center}
.quote-art cite{display:block;text-align:center;color:var(--orange);font:600 16px "Montserrat",sans-serif;letter-spacing:3px;margin-top:24px;font-style:normal}
.quote-card figcaption{color:var(--purple);font:700 21px/1.4 "Montserrat",sans-serif;text-align:center;margin-top:20px}

/* Books */
.books{position:absolute;top:3600px;left:0;width:1200px;height:430px;background:linear-gradient(90deg,var(--purple-deep),var(--purple) 60%,var(--magenta))}
.book{position:absolute;left:250px;top:-80px;width:290px;height:440px;background:linear-gradient(135deg,#4b1a6b,#7a2a8d);box-shadow:14px 14px 30px rgba(0,0,0,.35);padding:120px 30px 0;color:var(--white);text-align:center}
.book .brand{position:static;justify-content:center;font-size:26px;color:var(--white)}
.book span{display:block;font:800 20px "Montserrat",sans-serif;margin-top:80px;letter-spacing:1px}
.books-text{position:absolute;left:620px;top:70px;width:500px;color:var(--white)}
.books-text h2{font-size:50px;line-height:1.05}
.books-text p{font-size:17px;line-height:1.55;margin-top:22px}
.chevron{position:absolute;left:570px;top:4020px}

/* Events */
.events{position:absolute;top:4080px;left:0;width:1200px;text-align:center}
.events h2{font-size:68px;color:var(--purple)}
.events p{font-size:17px;line-height:1.6;text-align:left;margin:20px 90px 0}
.event-info{font:700 21px/1.5 "Montserrat",sans-serif;color:var(--magenta);margin-top:26px}

/* Footer */
.footer{position:absolute;top:4840px;left:0;width:1200px;height:288px;background:var(--dark);color:#cfcfd6;text-align:center;padding-top:70px}
.footer-brand{font:700 40px "Montserrat",sans-serif;color:var(--white);display:inline-flex;align-items:center;gap:14px}
.footer-brand i{width:26px;height:26px;border-radius:50%;background:var(--orange);display:inline-block}
.footer-tag{font:600 14px "Montserrat",sans-serif;letter-spacing:4px;margin-top:8px}
.footer p{font-size:15px;margin-top:40px;line-height:1.5}
</style>
</head>
<body>

<header class="hero">
  <div class="hero-photo" role="img" aria-label="Silhouette of a woman jumping joyfully against a golden sunset sky"></div>
  <div class="hero-wash"></div>
  <div class="brand"><span class="brand-dot"></span>Tall Birch Path</div>
  <h1 class="hero-title caps">Tall Birch Path<br>Tips &amp; Tools</h1>
  <p class="hero-sub">See our Website For more Details</p>
  <a class="btn">Learn More ›</a>
  <div class="polaroid pol-a"><div role="img" aria-label="Snapshot of hands forming a heart against the sunset"></div></div>
  <div class="polaroid pol-b"><div role="img" aria-label="Snapshot of a family walking on the beach"></div></div>
  <svg class="hero-curve" width="1200" height="90" viewBox="0 0 1200 90">
    <path d="M0 60 Q600 -10 1200 40 L1200 90 L0 90Z" fill="#ffffff"/>
    <path d="M0 60 Q600 -10 1200 40" fill="none" stroke="#b0186e" stroke-width="6"/>
  </svg>
</header>

<section class="letter">
  <div class="quote-mark">“</div>
  <h2 class="greeting script">Hello Friends!!</h2>
  <p>I am excited to (hopefully) add a little love to your in-box with this newsletter. I love connecting with moms and helping them find tools to make their lives happier, more intentional, and more fun and this is a new way to do that!</p>
  <p>If you don't know me well, I am a certified Open Horizons Trainer and I lead coaching groups for moms. My OH workshops and Rising Moms Coaching Circle have the goal of fostering connections between amazing women and empowering moms with tools to build lives they are enthusiastic about living, on purpose – and that will be the goal of this newsletter, as well!</p>
  <p>I hope you find something useful and helpful and enjoy receiving this info (and if not, feel free to unsubscribe and my feelings will not be hurt!)</p>
  <div class="signoff script">With love, Maren</div>
</section>

<svg class="blob-right" width="140" height="300" viewBox="0 0 140 300"><path d="M140 0 Q20 60 60 160 Q90 240 140 300Z" fill="#f39a1e"/></svg>
<svg class="blob-left" width="90" height="220" viewBox="0 0 90 220"><path d="M0 0 Q90 110 0 220Z" fill="#5a1f7d" opacity=".25"/></svg>

<section class="building">
  <div class="building-photo" role="img" aria-label="Woman with open arms looking over a calm lake at dawn">
    <div class="brand"><span class="brand-dot"></span>Tall Birch Path</div>
  </div>
  <h2 class="section-band">Building Happiness</h2>
  <div class="building-text">
    <p>I firmly believe that thinking about your happiness is important and that happiness itself is a worthwhile goal! If you think about all the things you focus on in your life and all the goals you set for yourself, all of those things are leading you toward feeling happier. Happiness, in the end, is the ultimate goal.</p>
    <p>Of course, what makes each person happy is totally different – and that's awesome and one part of what makes life fun and exciting! Many happiness experts and authors note that the key ingredients in our lives that will make us happier are pursuing 2 categories:</p>
    <ul>
      <li>things that bring us pleasure (positive emotions) and</li>
      <li>things that bring us meaning &amp; fulfillment</li>
    </ul>
    <p>Give yourself a minute to think about (it's extra powerful if you write it down!) what makes YOU happy.</p>
  </div>
  <svg class="deco-swoosh" width="110" height="200" viewBox="0 0 110 200"><path d="M110 0 Q10 100 110 200Z" fill="#e0307e"/></svg>
</section>

<section class="questions">
  <div class="question">
    <h3 class="caps">What are things that make you feel happy / provide you with pleasure (little and big things!)?</h3>
    <p>For me: joking &amp; laughing with my kids &amp; husband, petting with my dog, sitting with a soft blanket and a book, my first sip of coffee in the morning, walking in nature, traveling, scuba diving, exercise classes, making my friends laugh.</p>
  </div>
  <div class="question">
    <h3 class="caps">What are things that are meaningful to you / make you feel fulfilled (little and big things!)?</h3>
    <p>For me: teaching Open Horizons workshops, spending quality time with my family, making gratitude lists, volunteering, leading moms' coaching groups, making my kids breakfast.</p>
  </div>
</section>

<section class="quotes">
  <figure class="quote-card">
    <div class="quote-art one" role="img" aria-label="Quote card over a photo of a misty forest path">
      <blockquote>Happiness is not something you postpone for the future; it is something you design for the present.</blockquote>
    </div>
    <figcaption>How could you add more of those things that bring you happiness to your days?</figcaption>
  </figure>
  <figure class="quote-card">
    <div class="quote-art two" role="img" aria-label="Quote card over a photo of a dark mountain landscape">
      <blockquote>Happiness cannot be traveled to, owned, earned, worn or consumed. Happiness is the spiritual experience of living every minute with love, grace, and gratitude.</blockquote>
      <cite>DANA WHITFIELD</cite>
    </div>
    <figcaption>Try to add 1 or 2 of those things per week and see how your happiness increases! You are worth it!</figcaption>
  </figure>
</section>

<section class="books">
  <div class="book">
    <div class="brand">Tall Birch Path</div>
    <span>TIPS &amp; TOOLS</span>
  </div>
  <div class="books-text">
    <h2 class="caps">Empowering<br>Books</h2>
    <p>I love to read uplifting, inspiring material. Each newsletter, I'll suggest a few books that I've enjoyed! The Joy Journal by Greta Rowan and You Are Unstoppable: How to Quiet Your Doubts and Start Living a Radiant Life by Jenna Sinclair.</p>
  </div>
</section>

<svg class="chevron" width="60" height="40" viewBox="0 0 60 40"><path d="M0 0 L30 30 L60 0" fill="none" stroke="#5a1f7d" stroke-width="6"/></svg>

<section class="events">
  <h2 class="script">Upcoming Events</h2>
  <p>I lead an Open Horizons Workshop 2-3 times per year. The next one is coming up in September/October. More details to come – but here is a little info... In September, the kids will be going back to school and you can spend time focusing on YOU. Let this be the year where you take time to focus on yourself so that you can feel amazing, focused, fulfilled, purposeful, and happier! Take the time to learn some simple tools to help you live a life you love, deliberately, instead of just juggling what comes at you and juggling your to-do list. In this workshop, you will be empowered to build a life you love.</p>
  <div class="event-info">
    Dates: 3 morning workshop<br>
    September 27, October 4, October 11<br>
    9:30 – 12:30<br>
    Maren's home in Cedar Hollow Heights<br>
    Interested? Email me: maren@tallbirchpath.example
  </div>
</section>

<footer class="footer">
  <div class="footer-brand"><i></i>Open Horizons</div>
  <div class="footer-tag">THE ART OF SHAPING YOUR LIFE</div>
  <p>Enjoy the rest of Summer Break! Savor each amazing day! How can you add<br>a little more HAPPY to your August?! Make the choice and do it!</p>
</footer>

</body>
</html>
```